Visitenkarten und Briefpapier
Zielgruppe
Beratung- Planung Baumanagement für Private Auftraggeber und Handelsunternehmen. Der Name Kalk.Tänzerin soll den kompetenten Wegbegleiter während aller Bauphasen ausdrücken.
Aufgabenstellung
Das bestehenden Logo soll etwas geändert werden. Zur Beurteilung des Siegerprojekts wird eine Visitenkarte und das Briefpapier Design nicht nur das Logo herangezogen.
Kalktänzerin soll, damit es auch für männliche Mitarbeiter passt, etwas abgeändert werden. (Kalktänzerinnen)
Zudem wünsche ich mir ein schlichteres -nicht farbiges- Erscheinungsbild. Der Adler als Erkennungszeichen eines Ziviltechnikers muss aber bleiben. Anstelle der Zusatztexte wie kreative Zuverlässigkeit -soll Ziviltechniker stehen.
Wir benötigen die Umgestaltung des Logos, die Gestaltung von Visitenkarten und Briefpapier.
Die Graphiken sind so zu übergeben, dass Name und Adresse selbstständig geändert werden können, bzw. auch in den CAD-Plänen eingearbeitet werden können.

```html
<!DOCTYPE html>
<html lang="de">
<head>
<meta charset="utf-8">
<title>Kalk.Tänzerinnen – Visitenkarte</title>
<link rel="stylesheet" href="https://fonts.googleapis.com/css2?family=Open+Sans:wght@300;400;700&display=swap">
<style>
  :root {
    --backdrop: #e4e5e7;
    --paper: #ffffff;
    --mint: #9ac3b9;
    --mint-dark: #7fae a3;
    --ink: #2b2b2b;
    --ink-soft: #555a5c;
    --rule: #c9cccd;
    --mark-grey: #8e9294;
  }
  * { box-sizing: border-box; margin: 0; padding: 0; }
  html, body {
    width: 1200px; height: 771px; overflow: hidden;
    background: var(--backdrop);
    font-family: "Open Sans", Arial, sans-serif;
    color: var(--ink);
  }
  .canvas {
    position: relative; width: 1200px; height: 771px;
    display: flex; align-items: center; justify-content: center; gap: 60px;
  }
  .card {
    width: 500px; height: 324px; position: relative;
    box-shadow: 0 6px 18px rgba(0,0,0,.12);
  }
  .card--front { background: var(--paper); padding: 34px 40px; }
  .card--back {
    background: var(--mint);
    display: flex; align-items: center; justify-content: center;
  }
  .contact__name { font-size: 22px; font-weight: 700; line-height: 1.1; }
  .contact__surname { color: var(--mint); }
  .contact__title { font-size: 12px; font-weight: 300; color: var(--ink-soft); margin-top: 2px; }
  .contact__list { margin-top: 12px; font-size: 12px; line-height: 1.45; color: var(--ink-soft); }
  .contact__list dt { display: inline; font-weight: 700; color: var(--ink); }
  .contact__list dd { display: inline; font-weight: 400; }
  .contact__list .gap { margin-top: 10px; }
  .divider { border: 0; border-top: 1px solid var(--rule); margin-top: 14px; }
  .brand { display: flex; align-items: center; gap: 12px; }
  .brand__mark { width: 34px; height: 34px; border-radius: 50%; flex: none; }
  .brand__text { display: flex; flex-direction: column; }
  .brand__name {
    font-weight: 300; font-size: 30px; line-height: 1.05; letter-spacing: .5px;
    border-bottom: 1px solid currentColor; padding-bottom: 3px;
  }
  .brand__tagline { font-size: 11px; font-weight: 300; margin-top: 3px; text-align: right; }
  .card--front .brand { position: absolute; left: 150px; bottom: 38px; }
  .card--front .brand__mark { background: var(--mark-grey); }
  .card--front .brand__name { color: var(--ink); }
  .card--front .brand__tagline { color: var(--ink-soft); }
  .card--back .brand__mark { background: #ffffff; }
  .card--back .brand__name, .card--back .brand__tagline { color: #ffffff; }
</style>
</head>
<body>
<main class="canvas">
  <section class="card card--front" aria-label="Visitenkarte Vorderseite">
    <h1 class="contact__name">Marlene <span class="contact__surname">Hofbauer</span></h1>
    <p class="contact__title">Ziviltechniker Arch. DI</p>
    <dl class="contact__list">
      <div><dt>Büro:</dt> <dd>Lindengasse 17, 1070 Wien</dd></div>
      <div class="gap"><dt>Telefon:</dt> <dd>+43 660 5827193</dd></div>
      <div><dt>Telefax:</dt> <dd>+43 1 4862590</dd></div>
      <div><dt>E-Mail:</dt> <dd>marlene.hofbauer@kalk-taenzerin.at</dd></div>
    </dl>
    <hr class="divider">
    <div class="brand">
      <span class="brand__mark" aria-hidden="true"></span>
      <div class="brand__text">
        <span class="brand__name">Kalk.Tänzerinnen</span>
        <span class="brand__tagline">Ziviltechniker Arch. DI Marlene Hofbauer</span>
      </div>
    </div>
  </section>

  <section class="card card--back" aria-label="Visitenkarte Rückseite">
    <div class="brand">
      <span class="brand__mark" aria-hidden="true"></span>
      <div class="brand__text">
        <span class="brand__name">Kalk.Tänzerinnen</span>
        <span class="brand__tagline">Ziviltechniker Arch. DI Marlene Hofbauer</span>
      </div>
    </div>
  </section>
</main>
</body>
</html>
```